Healer at the Hearth needs business card

We need a business card that reflects the look and feel of the new website at www.healerathehearth.ca

Our patient navigation and advocacy services are most commonly used by seniors who feel overwhelmed by the health care system and want someone on their side to advocate for their care. Individuals with ill parents or other family members may also come to rely on Healer at the Hearth to help them support their loved one through their health care journey. Ultimately, anyone who finds their health care experience challenging and wants someone completely focused on their needs can benefit from the services of our doctor / nurse team.

Business

Must have
• One design tailored for two clinician which should include: logo, name, title, tel, email, web address and tagline
Nice to have
• A banner image to create a similar look to the website at www.healerathehearth.ca
Should not have
• Too cluttered or busy - must be clean and professional

```html
<!DOCTYPE html>
<html lang="en">
<head>
<meta charset="utf-8">
<title>Healer at the Hearth — Business Card</title>
<link href="https://fonts.googleapis.com/css2?family=Fira+Sans:wght@300;400&display=swap" rel="stylesheet">
<style>
  :root {
    --stage: #e4e5e7;
    --brand-blue: #16678f;
    --text-blue: #1b6a90;
    --ink: #3b3b3b;
    --paper: #ffffff;
    --apple-red: #a51d26;
  }
  html, body {
    margin: 0;
    padding: 0;
    width: 1200px;
    height: 900px;
    overflow: hidden;
    background: var(--stage);
    font-family: "Fira Sans", Arial, sans-serif;
  }
  .canvas {
    position: relative;
    width: 1200px;
    height: 900px;
  }
  .card {
    position: absolute;
    top: 304px;
    width: 492px;
    height: 282px;
    background: var(--paper);
    overflow: hidden;
  }
  .card--front { left: 110px; background: var(--brand-blue); }
  .card--back { left: 613px; }

  .front-name {
    position: absolute;
    left: 29px;
    top: 62px;
    margin: 0;
    color: var(--paper);
    font-weight: 300;
    font-size: 30px;
    line-height: 38px;
  }
  .front-banner {
    position: absolute;
    left: 0;
    top: 179px;
    width: 492px;
    height: 80px;
    background: linear-gradient(90deg, #e9ecee 0%, #f7f8f9 35%, #b83a3a 50%, #f4f5f6 62%, #e6e9eb 100%);
  }

  .brand {
    position: absolute;
    left: 27px;
    top: 94px;
    display: flex;
    align-items: center;
    gap: 11px;
  }
  .brand-dot {
    width: 78px;
    height: 78px;
    border-radius: 50%;
    background: var(--apple-red);
    flex: none;
  }
  .brand-name {
    margin: 0;
    color: var(--text-blue);
    font-weight: 400;
    font-size: 25px;
    line-height: 32px;
  }

  .details {
    position: absolute;
    left: 291px;
    top: 78px;
    width: 190px;
  }
  .details-title {
    margin: 0 0 14px;
    color: var(--text-blue);
    font-weight: 400;
    font-size: 20px;
    line-height: 24px;
  }
  .contact {
    margin: 0;
    font-size: 11.5px;
    line-height: 14px;
    color: var(--ink);
  }
  .contact-label { color: var(--text-blue); }
  .tagline {
    margin: 14px 0 0;
    font-size: 11.5px;
    line-height: 14px;
    color: var(--text-blue);
  }
</style>
</head>
<body>
<main class="canvas">
  <section class="card card--front">
    <h1 class="front-name">Healer at<br>the Hearth</h1>
    <div class="front-banner" role="img" aria-label="Photo of a doctor in a white coat with a stethoscope holding a red heart"></div>
  </section>

  <section class="card card--back">
    <div class="brand">
      <span class="brand-dot" aria-hidden="true"></span>
      <p class="brand-name">Healer at<br>the Hearth</p>
    </div>
    <div class="details">
      <h2 class="details-title">Title here</h2>
      <p class="contact"><span class="contact-label">tel:</span> +01 98 7654 3210</p>
      <p class="contact"><span class="contact-label">email:</span> hello@healerathehearth.ca</p>
      <p class="contact"><span class="contact-label">web:</span> www.healerathehearth.ca</p>
      <p class="tagline">Tagline here,tagline here tagline here</p>
    </div>
  </section>
</main>
</body>
</html>
```